"Road work ahead" Paving Business card design

We own a paving business residential and commercial. We want to appeal to small homeowner and also to a larger professional company - driveway to home and parking lot. We also like dump trucks.The asphalt look is important that is what we mainly do.

Target Market(s)

Residential and Commercial

Industry/Entity Type

Business

Contact Information for Business Card

Company info. (address, email, phone number)

Font styles to use
Sans Serif
Decorative

Colors
ec1f27
fbee3f
1b1b1b
474747

Requirements
Must have
• Business Logo/Name
• address: 4187 North Calder Lane
• Linden Falls, MD 21799
• business phone: 240.555.0193
• office: 301.555.0147
• fax: 301.555.0162
• www.TQSurfacing.example
• Maryland's #1 Asphalt Specialist
• MHIC# 384072
• All Work Guaranteed
• Residential & Commercial
• Include: Roads-Driveways-Brick Pavers- Seal-Coating-Concrete-Asphalt Millings
• "Serving Central Maryland for over 15 years"
Nice to have
• Real life pictures that were included. The backround can be cut out if it doesn't look professional on the pictures they are not photo shopped. Would like to see the picture of all 3 trucks on the front of the card.

```html
<!DOCTYPE html>
<html lang="en">
<head>
<meta charset="utf-8">
<title>TQ Surfacing — Business Card</title>
<link href="https://fonts.googleapis.com/css2?family=Source+Sans+3:ital,wght@0,400;0,600;1,400;1,600&display=swap" rel="stylesheet">
<style>
  :root {
    --red: #ec1f27;
    --red-deep: #7a0d12;
    --yellow: #fbee3f;
    --gold: #d9b21c;
    --ink: #1b1b1b;
    --slate: #474747;
    --paper: #f4f5f6;
    --stage: #dcd8d2;
    --white: #ffffff;
  }
  * { box-sizing: border-box; margin: 0; padding: 0; }
  html, body { width: 1200px; height: 685px; overflow: hidden; }
  body {
    background: var(--stage);
    font-family: "Source Sans 3", sans-serif;
    display: flex; align-items: center; justify-content: center; gap: 40px;
  }
  .card {
    position: relative; width: 500px; height: 286px;
    border-radius: 16px; overflow: hidden;
    background: linear-gradient(180deg, var(--white) 0%, var(--paper) 55%);
    box-shadow: 0 6px 18px rgba(0,0,0,.18);
  }
  .card-band { position: absolute; inset: 0; width: 100%; height: 100%; }
  .brand {
    position: absolute; left: 0; right: 0; top: 44px;
    display: flex; align-items: center; justify-content: center; gap: 12px;
  }
  .brand-name {
    font-weight: 600; font-size: 40px; letter-spacing: 1px; color: var(--red-deep);
  }
  .brand-dot { width: 58px; height: 58px; border-radius: 50%; background: var(--red-deep); }
  .card-back .brand-name { color: #b9a9a9; }
  .card-back .brand-dot { background: #c9b3b3; }

  /* front */
  .identity { position: absolute; right: 252px; top: 196px; text-align: right; }
  .person { color: var(--yellow); font-size: 21px; letter-spacing: .5px; margin-bottom: 8px; }
  .address { color: #f1d9d9; font-size: 14.5px; line-height: 18px; white-space: nowrap; }
  .divider { position: absolute; left: 262px; top: 194px; width: 1px; height: 68px; background: var(--gold); }
  .contacts { position: absolute; left: 274px; top: 194px; list-style: none; }
  .contacts li { display: flex; align-items: center; gap: 7px; color: var(--white); font-size: 14.5px; line-height: 19px; white-space: nowrap; }
  .contacts svg { width: 12px; height: 12px; fill: var(--yellow); flex: none; }

  /* back */
  .tagline {
    position: absolute; left: 24px; right: 18px; top: 182px;
    display: flex; align-items: center; gap: 6px;
    color: var(--gold); font-weight: 600; font-size: 16.5px; white-space: nowrap;
  }
  .tagline::before, .tagline::after { content: ""; flex: 1; height: 1px; background: #f0d9a0; }
  .credentials { position: absolute; left: 24px; top: 212px; list-style: none; }
  .credentials li, .services li { font-style: italic; color: #f1dcdc; font-size: 14px; line-height: 17px; white-space: nowrap; }
  .credentials li::before { content: "•"; color: var(--gold); margin-right: 6px; font-style: normal; }
  .services-head { position: absolute; right: 18px; top: 204px; color: var(--gold); font-weight: 600; font-size: 14.5px; }
  .services { position: absolute; right: 18px; top: 222px; list-style: none; text-align: right; }
  .services .sep { color: var(--gold); font-style: normal; margin: 0 3px; }
</style>
</head>
<body>
  <svg width="0" height="0" style="position:absolute">
    <defs>
      <radialGradient id="band-red" cx="35%" cy="75%" r="75%">
        <stop offset="0" stop-color="#e0232b"/>
        <stop offset=".55" stop-color="#a4141a"/>
        <stop offset="1" stop-color="#5e0a0e"/>
      </radialGradient>
      <symbol id="band" viewBox="0 0 500 286" preserveAspectRatio="none">
        <path d="M0,160 C130,198 270,182 500,142 L500,286 L0,286 Z" fill="url(#band-red)"/>
        <path d="M0,146 C90,172 200,184 300,174 C200,190 90,184 0,158 Z" fill="var(--gold)"/>
        <path d="M228,174 C320,150 420,140 500,140 L500,160 C420,156 320,162 228,174 Z" fill="var(--ink)"/>
      </symbol>
      <symbol id="icon-phone" viewBox="0 0 24 24"><path d="M6.6 10.8a15 15 0 0 0 6.6 6.6l2.2-2.2c.3-.3.7-.4 1-.2 1.1.4 2.3.6 3.6.6.6 0 1 .4 1 1V20c0 .6-.4 1-1 1A17 17 0 0 1 3 4c0-.6.4-1 1-1h3.5c.6 0 1 .4 1 1 0 1.3.2 2.5.6 3.6.1.3 0 .7-.2 1z"/></symbol>
      <symbol id="icon-fax" viewBox="0 0 24 24"><path d="M6 2h12v6H6zM3 9h18v9h-3v4H6v-4H3zm5 7v4h8v-4z"/></symbol>
      <symbol id="icon-web" viewBox="0 0 24 24"><path d="M12 2a10 10 0 1 0 0 20 10 10 0 0 0 0-20zm0 3a7 7 0 0 1 6.7 5H5.3A7 7 0 0 1 12 5zm0 14a7 7 0 0 1-6.7-5h13.4A7 7 0 0 1 12 19z"/></symbol>
    </defs>
  </svg>

  <article class="card card-front">
    <svg class="card-band" aria-hidden="true"><use href="#band"/></svg>
    <div class="brand"><span class="brand-name">TQ SURFACING</span><span class="brand-dot"></span></div>
    <div class="identity">
      <p class="person">DANIEL REYES</p>
      <p class="address">4187 North Calder Lane<br>Linden Falls, MD 21799</p>
    </div>
    <span class="divider"></span>
    <ul class="contacts">
      <li><svg><use href="#icon-phone"/></svg>240.555.0193</li>
      <li><svg><use href="#icon-phone"/></svg>301.555.0147</li>
      <li><svg><use href="#icon-fax"/></svg>301.555.0162</li>
      <li><svg><use href="#icon-web"/></svg>www.TQSurfacing.example</li>
    </ul>
  </article>

  <article class="card card-back">
    <svg class="card-band" aria-hidden="true" style="transform:scaleX(-1)"><use href="#band"/></svg>
    <div class="brand"><span class="brand-dot"></span><span class="brand-name">TQ SURFACING</span></div>
    <p class="tagline">Serving Central Maryland for over 15 years</p>
    <ul class="credentials">
      <li>Maryland's #1 Asphalt Specialist</li>
      <li>MHIC# 384072</li>
      <li>All Work Guaranteed</li>
      <li>Residential &amp; Commercial</li>
    </ul>
    <p class="services-head">Include :</p>
    <ul class="services">
      <li>Roads<span class="sep">•</span>Driveways</li>
      <li>Brick Pavers<span class="sep">•</span>Seal-Coating</li>
      <li>Concrete<span class="sep">•</span>Asphalt Millings</li>
    </ul>
  </article>
</body>
</html>
```